Profesional personal website needs design and business card

I need a business card with my professional name as a logo "Orlan Vitality" for my business. I am a Wellness Coach, consultant and trainer. So it should be professional, wellness oriented and modern.

Target Market(s)

Private clients, governments, corporations. Luxury and high market.

Industry/Entity Type

Health And Wellness

Contact Information for Business Card

Orlan Vitality should be the logo

Colors

Designer to choose colors to be used in the design.

Requirements
Must have
• Orlan Vitality
• Name: Dario Montalbe
• Wellness Coach, Consultant & Trainer.
• Website: www.orlanvitality-example.com
• Phone:
• Spain (+34) 612 480 597
• (USA) +1 (555) 318 0264
Nice to have
• The most important is the design of "Orlan Vitality", as this is going to be my personal brand logo. It should be professional, wellness, high end and actual.
Should not have
• no golds, no baroque style..

```html
<!DOCTYPE html>
<html lang="en">
<head>
<meta charset="utf-8">
<title>Orlan Vitality – Business Card</title>
<link rel="stylesheet" href="https://fonts.googleapis.com/css2?family=Arimo:wght@400;700&display=swap">
<style>
  :root {
    --page-bg: #d9d4cc;
    --card-top: #eef0ea;
    --card-bottom: #dfe3da;
    --card-edge: #ffffff;
    --brand-green: #1f6b1f;
    --rule-green: #2f7d2a;
    --ink: #2a2a2a;
  }
  html, body {
    margin: 0;
    padding: 0;
    width: 1200px;
    height: 969px;
    overflow: hidden;
    background: var(--page-bg);
    font-family: "Arimo", Arial, sans-serif;
  }
  .card {
    position: absolute;
    left: 141px;
    top: 224px;
    width: 918px;
    height: 522px;
    border-radius: 26px;
    background: linear-gradient(160deg, var(--card-top), var(--card-bottom));
    border: 1px solid var(--card-edge);
    box-shadow: 0 4px 14px rgba(0,0,0,0.12);
    text-align: center;
    color: var(--ink);
  }
  .brand-logo {
    position: absolute;
    left: 0;
    right: 0;
    top: 98px;
    margin: 0;
    font-weight: 700;
    font-size: 58px;
    line-height: 54px;
    letter-spacing: 2px;
    color: var(--brand-green);
    text-transform: uppercase;
  }
  .person-name {
    position: absolute;
    left: 0; right: 0;
    top: 266px;
    margin: 0;
    font-weight: 700;
    font-size: 26px;
    color: var(--brand-green);
    text-transform: uppercase;
  }
  .person-title {
    position: absolute;
    left: 0; right: 0;
    top: 304px;
    margin: 0;
    font-size: 17px;
    text-transform: uppercase;
  }
  .rule {
    position: absolute;
    left: 150px;
    width: 620px;
    height: 0;
    border-top: 1.5px solid var(--rule-green);
  }
  .rule-upper { top: 338px; }
  .rule-lower { top: 397px; }
  .contact-phones {
    position: absolute;
    left: 0; right: 0;
    top: 355px;
    margin: 0;
    font-size: 19px;
    white-space: nowrap;
  }
  .contact-web {
    position: absolute;
    left: 40px; right: 0;
    top: 414px;
    margin: 0;
    font-size: 18px;
    text-transform: uppercase;
  }
</style>
</head>
<body>
  <div class="card">
    <h1 class="brand-logo">Orlan<br>Vitality</h1>
    <p class="person-name">Dario Montalbe</p>
    <p class="person-title">Wellness Coach, Consultant &amp; Trainer</p>
    <div class="rule rule-upper"></div>
    <p class="contact-phones">PH : (+34) 612 480 597 SPAIN&nbsp;&nbsp;PH : +1 (555) 318 0264 (USA)</p>
    <div class="rule rule-lower"></div>
    <p class="contact-web">www.orlanvitality-example.com</p>
  </div>
</body>
</html>
```